Printed magazine advertisement for a book about piano styles.

Hello all,

I need a design for an ad:

Goal: I am trying to promote my book about various national styles of playing classical piano.

1. Ad will be printed in several piano-related magazines, here are examples:

http://www.brackenmoor.co.uk/brackenmoor-publishing/magazines/silver-lantern/
http://www.qvlr.org/
https://www.harborlightjournal.com/

2. I would like to ask for a design that can be adjusted to 3 size specifications so that I can post it in magazines (please see 'File specifications' attachment).

3. To save you time, please create a design in a single format. If successful, we can then adjust it to other specifications.

4. Here is my website this discusses the book: http://thornfieldvellum.com/

5. If possible, the design should include:
- QRS code
- Zentora logo (book is available through Zentora, please pick logo version suitable to your design)
- Book cover (it can include only the front page, up to your discretion)
- Blurb (see 'Ad blurb')

7. The character of the ad should be: classy, trustworthy, professional

Please let me know if there are any issues with fitting all the required text into the specified size. I can try to make it shorter.

Thank you for your interest.

Piano professionals, pianists, teachers, academic researchers

• All must haves are already described in Project description.

```html
<!DOCTYPE html>
<html lang="en">
<head>
<meta charset="utf-8">
<title>Mapping Regional Piano Lineages – Advertisement</title>
<link href="https://fonts.googleapis.com/css2?family=Cinzel:wght@400&family=EB+Garamond:wght@400;600&display=swap" rel="stylesheet">
<style>
  :root {
    --page: #ffffff;
    --ad-black: #0f1112;
    --text-white: #f4f4f2;
    --frame: #f2f2f2;
    --link-orange: #d98a1c;
    --cover-blue: #6f8296;
    --cover-dark: #1e2530;
  }
  * { margin: 0; padding: 0; box-sizing: border-box; }
  html, body {
    width: 1200px; height: 1200px; overflow: hidden;
    background: var(--page);
  }
  .canvas { position: relative; width: 1200px; height: 1200px; }
  .ad {
    position: absolute; left: 39px; top: 250px;
    width: 1123px; height: 699px;
    background: var(--ad-black);
    overflow: hidden;
    font-family: "EB Garamond", Georgia, serif;
    color: var(--text-white);
  }
  .ad__photo {
    position: absolute; inset: 0;
    background:
      radial-gradient(ellipse 55% 30% at 30% 2%, #d9dadb 0%, #7d7f80 40%, transparent 75%),
      linear-gradient(155deg, transparent 0%, transparent 32%, rgba(110,112,114,.45) 46%, transparent 62%),
      linear-gradient(90deg, #9a9c9d 0%, #3a3c3e 12%, #17191a 24%, var(--ad-black) 60%);
  }
  .blurb {
    position: absolute; left: 195px; top: 67px; width: 730px;
    font-size: 22px; line-height: 26.4px;
    letter-spacing: 1.1px;
    text-align: justify;
  }
  .title-frame {
    position: absolute; left: 198px; top: 244px;
    width: 727px; height: 220px;
    border: 2px solid var(--frame);
    text-align: center;
  }
  .title-frame__kicker {
    font-family: "Cinzel", "Trajan Pro", serif;
    font-weight: 400;
    font-size: 48px; line-height: 1; margin-top: 32px;
    letter-spacing: .5px;
  }
  .title-frame__main {
    font-family: "Cinzel", "Trajan Pro", serif;
    font-weight: 400;
    font-size: 78px; line-height: 1; margin-top: 6px;
    text-shadow: 0 2px 6px rgba(0,0,0,.6);
  }
  .title-frame__sub {
    font-size: 25px; margin-top: 12px; letter-spacing: 1px;
  }
  .quote {
    position: absolute; left: 195px; top: 506px; width: 700px;
    font-size: 22px; line-height: 26.4px;
    letter-spacing: .9px;
  }
  .website {
    position: absolute; left: 195px; top: 624px;
    font-size: 22px; letter-spacing: .8px;
    color: var(--link-orange);
    text-decoration: none;
  }
  .retailer {
    position: absolute; left: 800px; top: 617px;
    line-height: 1;
  }
  .retailer__label { font-size: 11px; display: block; margin-bottom: 3px; }
  .retailer__name { font-size: 24px; font-weight: 600; }
  .book-cover {
    position: absolute; left: 917px; top: 426px;
    width: 152px; height: 238px;
    background: linear-gradient(170deg, var(--cover-blue) 0%, #3f4c5c 40%, var(--cover-dark) 100%);
    box-shadow: 4px 4px 10px rgba(0,0,0,.6);
    border-right: 2px solid #d8dadc;
  }
</style>
</head>
<body>
<div class="canvas">
  <section class="ad">
    <div class="ad__photo" role="img" aria-label="Close-up photograph of a grand piano keyboard and curved lid in black and white"></div>

    <p class="blurb">This book is the result of a six-year doctoral investigation into the phenomenon of ‘national piano schools’. It describes the current state and evolution of Russian, Austro-German and French piano styles amongst others, and identifies key areas through which the schools may be defined (such as history, language, technique, and cultural heritage).</p>

    <div class="title-frame">
      <h1 class="title-frame__kicker">Mapping Regional</h1>
      <p class="title-frame__main">Piano Lineages</p>
      <p class="title-frame__sub">Voices and directions - Dr Marek Zielinski</p>
    </div>

    <blockquote class="quote">“Pianists often trace their lineage back to, for example, Hollander. But I think through changes in society, migration of the people, the whole change of attitude, I do not think there is anything left of that Hollander tradition.” (Interview 4) (Chapter 6)</blockquote>

    <a class="website" href="http://thornfieldvellum.com/">www.thornfieldvellum.com</a>

    <div class="retailer">
      <span class="retailer__label">Available at</span>
      <span class="retailer__name">Zentora</span>
    </div>

    <div class="book-cover" role="img" aria-label="Front cover of the book Mapping Regional Piano Lineages by Marek Zielinski"></div>
  </section>
</div>
</body>
</html>
```